Accountancy practice needs a wordpress website redesign for growth

We are a growing accountancy practice - headcount and revenues have doubled in the last 2 years. We are continuing to grow. We only had a website made around 12 months ago but the company we used offered very little in terms of creativity and ideas of how to make it look modern and eye-catching. We want to redesign the website to make it look premium and professional because we are starting to launch more marketing and drive more traffic to the site.

The current website is www.tolvardaccountants.co.uk. The website was built in wordpress.

The logo has been uploaded. The main 2 colour hex codes are: 0E74BC and 14A79D.

We are open to changing the fonts in the website and welcome suggestions for this too.

Following on from this we will launch a project to design brochures and one-page flyers that we can fill with useful information about what we do and also create lead-generators to download from the website. So the design of the website will influence the overall brand and feel of all of the marketing collateral.

Target Market(s)

Property businesses and entrepreneurial, growth mindset clients

Industry/Entity Type

Accountancy

Number of Pages Required

3 page

Font styles to use
Sans Serif

Colors

Designer to choose colors to be used in the design.

Requirements
Must have
• A modern and professional feel. 3 fonts - most websites seem to use 3 different fonts now and I like this. We have our green and blue colours but I do not want too much of this all over the site, stick to blacks, whites and greys with the blue and green used for emphasis and accents.
Nice to have
• The coloured spaces should have some "depth" to them, eg a small pattern in the white spaces so its not just a solid whie background.

```html
<!DOCTYPE html>
<html lang="en">
<head>
<meta charset="utf-8">
<title>Tolvard Accountants</title>
<link href="https://fonts.googleapis.com/css2?family=Roboto+Condensed:wght@700&family=Poppins:wght@400;500;600&family=Montserrat:wght@600;700&display=swap" rel="stylesheet">
<style>
:root{
  --blue:#0E74BC;
  --teal:#14A79D;
  --ink:#111418;
  --text:#6d7278;
  --grey:#f3f4f5;
  --navy:#0c2c55;
  --white:#fff;
}
*{box-sizing:border-box;margin:0;padding:0}
html,body{width:1200px;height:4666px;overflow:hidden}
body{font-family:"Poppins",sans-serif;color:var(--text);background:var(--white);position:relative}
.section{position:absolute;left:0;width:1200px;overflow:hidden}
.abs{position:absolute}
h1,h2,h3{font-family:"Roboto Condensed",sans-serif;font-weight:700;color:var(--ink)}
.btn{position:absolute;display:flex;align-items:center;justify-content:center;background:var(--teal);color:#fff;font-family:"Montserrat",sans-serif;font-weight:700;font-size:10px;letter-spacing:.3px;text-transform:uppercase;border-radius:2px}
.photo{position:absolute}
.topbar{top:0;height:31px;background:var(--blue)}
.topbar span{position:absolute;top:10px;color:#fff;font-family:"Montserrat",sans-serif;font-size:9px;font-weight:700}
.topbar .divider{position:absolute;top:0;left:983px;width:1px;height:31px;background:rgba(255,255,255,.4)}
.nav{top:31px;height:72px;background:#fff}
.brand{position:absolute;display:flex;align-items:center;gap:8px;font-family:"Poppins",sans-serif;font-weight:600;color:var(--blue);font-size:19px;letter-spacing:.5px}
.brand i{display:block;width:20px;height:20px;background:var(--teal);border-radius:50%}
.nav-links{position:absolute;left:450px;top:29px;display:flex;gap:30px;font-family:"Montserrat",sans-serif;font-size:10px;font-weight:700;color:var(--ink)}
.hero{top:103px;height:518px;background:linear-gradient(100deg,#1a4d86 0%,#2c78bb 40%,#6aa8d8 70%,#9fc8ea 100%)}
.hero h1{position:absolute;left:112px;top:145px;color:#fff;font-size:45px;line-height:57px;width:490px}
.about{top:621px;height:505px}
.about h2{position:absolute;left:112px;top:94px;font-size:36px}
.about p{position:absolute;left:112px;font-size:10px;line-height:19px;width:440px}
.stat{position:absolute;left:563px;top:284px;width:197px;height:145px;background:#fff;box-shadow:0 6px 24px rgba(0,0,0,.1);text-align:center;padding-top:38px}
.stat b{display:block;font-family:"Roboto Condensed",sans-serif;font-size:36px;color:var(--blue)}
.stat span{font-size:13px;color:var(--teal);font-weight:500}
.software{top:1126px;height:481px;background:var(--grey)}
.center-title{position:absolute;left:0;width:1200px;text-align:center;font-size:36px}
.center-text{position:absolute;left:260px;width:680px;text-align:center;font-size:10.5px;line-height:19px}
.logo-card{position:absolute;top:197px;width:147px;height:152px;background:#fff;display:flex;align-items:center;justify-content:center;font-family:"Poppins",sans-serif;font-weight:600;font-size:15px;color:var(--ink)}
.help{top:1607px;height:616px;background:linear-gradient(135deg,#0b4f93,#0E74BC 55%,#0a5fa3)}
.help h2{color:#fff}
.help-card{position:absolute;top:140px;width:235px;height:403px;border:2px solid rgba(255,255,255,.85)}
.help-card .photo{left:14px;top:14px;width:203px;height:150px}
.help-card .icon{position:absolute;left:94px;top:130px;width:46px;height:46px;border-radius:50%;background:#fff;display:flex;align-items:center;justify-content:center}
.help-card h3{position:absolute;top:196px;left:10px;width:211px;text-align:center;color:#fff;font-family:"Poppins",sans-serif;font-weight:600;font-size:13px;line-height:22px}
.help-card p{position:absolute;top:265px;left:22px;width:187px;text-align:center;color:#fff;font-size:10px;line-height:15px}
.why{top:2223px;height:700px}
.why h2{position:absolute;left:653px;top:78px;font-size:36px}
.why p{position:absolute;left:653px;width:432px;font-size:10px;line-height:18px}
.why ul{position:absolute;left:653px;top:380px;width:432px;list-style:none;font-size:10px;line-height:18.5px}
.why li{position:relative;padding-left:22px;margin-bottom:12px}
.why li:before{content:"";position:absolute;left:0;top:5px;width:8px;height:8px;border-radius:50%;background:var(--blue)}
.reviews{top:2923px;height:462px;background:#fbfbfb}
.review{position:absolute;top:136px;width:440px;height:236px;background:#fff;box-shadow:0 4px 18px rgba(0,0,0,.06);text-align:center;padding:24px 28px}
.review h4{font-family:"Poppins",sans-serif;font-weight:600;font-size:13px;color:var(--ink)}
.stars{color:#f6b400;font-size:15px;letter-spacing:1px;margin:6px 0 22px}
.review p{font-size:10px;line-height:18.5px}
.dots{position:absolute;top:418px;left:564px;display:flex;gap:22px}
.dots i{width:8px;height:8px;border-radius:50%;background:#b9dcd9}
.dots i.on{background:var(--teal)}
.insights{top:3385px;height:733px}
.post{position:absolute;top:135px;width:313px;height:444px;background:#fff;box-shadow:0 4px 20px rgba(0,0,0,.07)}
.post .photo{left:0;top:0;width:313px;height:186px}
.post h4{position:absolute;left:30px;top:210px;width:260px;font-family:"Poppins",sans-serif;font-weight:600;font-size:11px;line-height:22px;color:var(--ink)}
.post p{position:absolute;left:30px;top:290px;width:260px;font-size:10px;line-height:18px}
.post .more{position:absolute;left:30px;top:408px;font-size:10px;font-weight:600;color:var(--teal)}
.cta{top:4118px;height:259px;background:var(--teal);text-align:center}
.cta h2{position:absolute;left:0;width:1200px;top:57px;color:#fff;font-size:36px}
.cta h3{position:absolute;left:0;width:1200px;top:114px;color:#fff;font-family:"Poppins",sans-serif;font-weight:600;font-size:19px}
.footer{top:4377px;height:289px;background:var(--navy);color:#cdd7e4}
.footer h5{position:absolute;top:48px;font-family:"Poppins",sans-serif;font-size:13px;font-weight:600;color:#fff}
.footer ul{position:absolute;top:78px;list-style:none;font-size:8.5px;line-height:18px;color:#dfe6ef}
.footer .contact{position:absolute;left:668px;top:46px;width:150px;font-size:8px;line-height:14px;color:#dfe6ef}
.footer .contact div{display:flex;gap:8px;margin-bottom:10px}
.footer .legal{position:absolute;left:0;width:1200px;top:259px;text-align:center;font-family:"Montserrat",sans-serif;font-size:8px;font-weight:700;color:#fff}
.footer .rule{position:absolute;left:112px;width:976px;top:245px;height:1px;background:rgba(255,255,255,.25)}
.input{position:absolute;left:853px;top:80px;width:235px;height:32px;border:1px solid rgba(255,255,255,.6);border-radius:2px;font-size:8px;color:#c5d0dd;padding:10px 14px}
</style>
</head>
<body>

<div class="section topbar">
  <span style="left:831px">CLIENT PORTAL LOGIN</span>
  <div class="divider"></div>
  <span style="left:998px">GET IN TOUCH</span>
</div>

<header class="section nav">
  <div class="brand" style="left:112px;top:24px"><i></i>TOLVARD</div>
  <nav class="nav-links">
    <span>ABOUT US ⌄</span><span>WHO WE HELP ⌄</span><span>THOUGHTS</span><span>SWITCHING ACCOUNTANTS</span>
  </nav>
  <div class="btn" style="left:918px;top:19px;width:170px;height:36px">Book a discovery call</div>
</header>

<section class="section hero">
  <div class="photo" role="img" aria-label="Hand holding a pen over financial charts and figures" style="left:0;top:0;width:1200px;height:518px;background:radial-gradient(ellipse at 80% 60%,rgba(255,255,255,.35),transparent 55%)"></div>
  <h1>Your Accounts Will Be Done.What Else Can We Do For You?</h1>
  <div class="btn" style="left:112px;top:364px;width:198px;height:40px">Book a discovery call now</div>
</section>

<section class="section about">
  <h2>Tolvard Accountants</h2>
  <p style="top:160px">We understand that running and growing your business takes an incredible amount of effort; you don’t want to be bogged down worrying about getting paperwork done on time. You want to know that the decisions you make are based on sound, correct advice and you want to be able to talk to someone you trust for that advice. So don’t worry — we will make sure your accounts and taxes are done.</p>
  <p style="top:276px">Let’s see what else we can do for you.</p>
  <div class="btn" style="left:112px;top:340px;width:135px;height:38px">Get in touch</div>
  <svg class="abs" style="left:740px;top:30px" width="100" height="70"><polygon points="50,0 100,70 0,70" fill="#0E74BC"/></svg>
  <div class="photo" role="img" aria-label="Smiling accountant in glasses and a suit" style="left:688px;top:95px;width:371px;height:334px;background:linear-gradient(160deg,#e8eef5,#b7c7d8 60%,#4f6785)"></div>
  <svg class="abs" style="left:930px;top:300px" width="170" height="200"><polygon points="170,100 85,200 85,0" fill="#14A79D"/></svg>
  <div class="stat"><b>30+</b><span>Years Experience</span></div>
</section>

<section class="section software">
  <svg class="abs" style="left:0;top:0" width="240" height="180" opacity=".6"><polygon points="120,0 240,180 0,180" fill="#e6e7e9"/></svg>
  <svg class="abs" style="left:1010px;top:300px" width="190" height="180" opacity=".6"><polygon points="190,0 190,180 40,90" fill="#e6e7e9"/></svg>
  <h2 class="center-title" style="top:42px">Software Solutions</h2>
  <p class="center-text" style="top:104px">We are proud to work with a range of software solutions to ensure your accountancy procedures are running as smoothly as possible. Software can make a significant difference to your business and through the use of these solutions we can save you time and money, whilst also improving your business efficiency.</p>
  <div class="logo-card" style="left:112px">Ledvora</div>
  <div class="logo-card" style="left:278px">Sumbrook</div>
  <div class="logo-card" style="left:444px">Fildera</div>
  <div class="logo-card" style="left:610px">Meetlyne</div>
  <div class="logo-card" style="left:776px">Pracvue</div>
  <div class="logo-card" style="left:942px">Quorvel</div>
  <div class="btn" style="left:533px;top:393px;width:134px;height:38px">Load more</div>
</section>

<section class="section help">
  <h2 class="center-title" style="top:52px">Who We Help?</h2>
  <div class="help-card" style="left:112px">
    <div class="photo" role="img" aria-label="Property investors meeting with estate agent" style="background:linear-gradient(150deg,#d9dfe6,#9aa9b8)"></div>
    <div class="icon"><svg width="22" height="22"><rect x="4" y="3" width="14" height="17" fill="none" stroke="#0E74BC" stroke-width="2"/><path d="M8 7h2M12 7h2M8 11h2M12 11h2M9 20v-4h4v4" stroke="#0E74BC" stroke-width="2"/></svg></div>
    <h3>Property Investors and Developers</h3>
    <p>Busy with your investments and need to ensure your accounts are in order?</p>
    <div class="btn" style="left:52px;top:340px;width:127px;height:34px">Find out more</div>
  </div>
  <div class="help-card" style="left:358px">
    <div class="photo" role="img" aria-label="Consultants in a meeting room" style="background:linear-gradient(150deg,#e4e0d8,#a79c8c)"></div>
    <div class="icon"><svg width="22" height="22"><circle cx="6" cy="7" r="3" fill="#0E74BC"/><circle cx="16" cy="7" r="3" fill="#0E74BC"/><rect x="2" y="12" width="18" height="6" fill="#0E74BC"/></svg></div>
    <h3>Consultants</h3>
    <p>Your time is precious. Allow us to free up more of your valuable time.</p>
    <div class="btn" style="left:52px;top:340px;width:127px;height:34px">Find out more</div>
  </div>
  <div class="help-card" style="left:604px">
    <div class="photo" role="img" aria-label="Medical professionals walking in a hospital" style="background:linear-gradient(150deg,#e6ecf1,#9fb2c4)"></div>
    <div class="icon"><svg width="22" height="22"><path d="M11 19C3 13 3 6 7 5c2-.5 3 1 4 2 1-1 2-2.5 4-2 4 1 4 8-4 14z" fill="#0E74BC"/></svg></div>
    <h3>Medical Professionals</h3>
    <p>We take care of you whilst you take care of your patients.</p>
    <div class="btn" style="left:52px;top:340px;width:127px;height:34px">Find out more</div>
  </div>
  <div class="help-card" style="left:850px">
    <div class="photo" role="img" aria-label="Business people shaking hands on a deal" style="background:linear-gradient(150deg,#dfe6e8,#7d8d95)"></div>
    <div class="icon"><svg width="22" height="22"><path d="M2 11l5-4 4 3 4-3 5 4-6 5-3-2-3 2z" fill="#0E74BC"/></svg></div>
    <h3>Buying or Selling a Business</h3>
    <p>When buying or selling a business you need to know you have the right people in your corner.</p>
    <div class="btn" style="left:52px;top:340px;width:127px;height:34px">Find out more</div>
  </div>
</section>

<section class="section why">
  <div class="photo" role="img" aria-label="Two colleagues reviewing documents at a laptop" style="left:112px;top:81px;width:460px;height:415px;background:linear-gradient(150deg,#eef0f2,#c9cfd6 60%,#8d98a4)"></div>
  <div class="abs" style="left:389px;top:459px;width:235px;height:169px;background:#fff;box-shadow:0 6px 24px rgba(0,0,0,.1);display:flex;align-items:center;justify-content:center">
    <div class="brand" style="position:static"><i></i>TOLVARD</div>
  </div>
  <svg class="abs" style="left:1060px;top:510px" width="140" height="150" opacity=".7"><polygon points="140,0 140,150 20,75" fill="#eceef0"/></svg>
  <h2>Why Choose Us?</h2>
  <p style="top:138px">At Tolvard Accountants, we know you are the kind of people who want to be successful and have the time to do the things you love doing and to see the people you love seeing.<br>To do that, you need to focus on the important issues in your business and know that the numbers and filing deadlines are taken care of. You also need to know that you are getting reliable feedback and advice that can be used to make decisions.<br>The problem is (and we hear it from a lot of people) that the current accountant only does numbers and nothing else, or they don’t reply to you, or they don’t offer any solutions, or… Whatever the problem is, the end result is you are micromanaging and not getting the results you want.</p>
  <p style="top:348px;color:var(--ink);font-weight:600">Relax, we’ve got this covered.</p>
  <ul>
    <li>We’re here at the end of the phone to talk you through those decisions – you’ll have a dedicated point of contact (you can even pick how senior you want your contact to be).</li>
    <li>We’ll make sure your deadlines aren’t missed.</li>
    <li>We’ll tell you if we think we aren’t doing things in the best way possible.</li>
    <li>We’ll even attend your board meetings, if you’d like, to get into the business and provide that detailed input you are looking for.</li>
  </ul>
  <div class="btn" style="left:653px;top:597px;width:135px;height:38px">Get in touch</div>
</section>

<section class="section reviews">
  <h2 class="center-title" style="top:53px">What Our Clients Says</h2>
  <div class="review" style="left:-80px"><h4>Ravi Sandhu</h4><div class="stars">★★★★★</div><p>Personal service &amp; advice has been key for me to set up my property business in the right way to be tax efficient &amp; aligned with my long term plans. Great service and would highly recommend to all.</p></div>
  <div class="review" style="left:380px"><h4>Mark Ellison</h4><div class="stars">★★★★★</div><p>“Could not recommend Tolvard &amp; Co enough. A great family run company that are very experienced &amp; professional. We have been clients since 2013, from start up till now.What we have been so impressed with is their interest in actually helping us, they always return a call or an email, or an invite to their offices.They have advised us important business decisions in the past &amp; we trust them implicitly.Carol Ellison”</p></div>
  <div class="review" style="left:840px"><h4>Peter Harwood</h4><div class="stars">★★★★★</div><p>“Having recently moved my company and personal accounts to Tolvard Accountants, I have found them very knowledgeable, helpful, and professional and efficient.In particular they have helped me set up my investment business in the right way.”</p></div>
  <div class="dots"><i></i><i class="on"></i><i></i></div>
</section>

<section class="section insights">
  <svg class="abs" style="left:0;top:200px" width="90" height="200" opacity=".7"><polygon points="0,0 90,100 0,200" fill="#eceef0"/></svg>
  <h2 class="center-title" style="top:57px">Latest Insights And Thoughts</h2>
  <div class="post" style="left:112px">
    <div class="photo" role="img" aria-label="Article banner: adviser in front of a petrol station price board" style="background:linear-gradient(160deg,#f4c542,#d8332b 55%,#7a1f1f)"></div>
    <h4>Spring Statement – Property Market Update– What does it mean for the property prices?</h4>
    <p>Raging inflation..Covid..Brexit..war in Ukraine..and Tax Receipts rising! How can this be and what does it mean for you as a business owner or Property Investor? Dev Kaler talks us through what this all means for business owners and the property market.</p>
    <span class="more">Read More ⟶</span>
  </div>
  <div class="post" style="left:443px">
    <div class="photo" role="img" aria-label="Article banner: adviser in front of a government building door" style="background:linear-gradient(160deg,#f4c542,#2b2b2b 55%,#111)"></div>
    <h4>5 Benefits Property Investors missed in the Chancellor’s Spring Statement</h4>
    <p>Did you know there were 5 policies in the spring statement that affect property investors which many people missed. Were you one of them? Dev Kaler is back again for a deep dive into the Chancellor’s Spring Statement and the</p>
    <span class="more">Read More ⟶</span>
  </div>
  <div class="post" style="left:774px">
    <div class="photo" role="img" aria-label="Article banner: houses under construction with scaffolding" style="background:linear-gradient(160deg,#f4c542,#a56a45 50%,#6f86a3)"></div>
    <h4>VAT – How to pay less VAT if you are a property developer</h4>
    <p>How to pay less tax &amp; VAT on your property development and make more profit on your property investment.<br>If you are a property investor you need to understand VAT 20%, 5%, zero rate, exempt to stop tax leakage</p>
    <span class="more">Read More ⟶</span>
  </div>
  <div class="btn" style="left:480px;top:636px;width:240px;height:38px">Check out our other free advice</div>
</section>

<section class="section cta">
  <h2>Set A Date Today To Speak To Our Team</h2>
  <h3>Book An Appointment</h3>
  <div class="btn" style="left:533px;top:165px;width:134px;height:40px;background:#fff;color:var(--teal)">Book now</div>
</section>

<footer class="section footer">
  <div class="brand" style="left:112px;top:44px;color:#fff"><i></i>TOLVARD</div>
  <div class="abs" style="left:112px;top:140px;width:68px;height:30px;background:#fff;border-radius:2px"></div>
  <div class="abs" style="left:190px;top:140px;width:70px;height:30px;border:1px solid rgba(255,255,255,.6);border-radius:2px"></div>
  <div class="abs" style="left:112px;top:185px;font-size:8px;color:#dfe6ef">© 2022 Tolvard Accountants</div>
  <h5 style="left:296px">ABOUT US</h5>
  <ul style="left:296px"><li>Meet The Team</li><li>Our Values</li><li>Software Solutions</li><li>Vacancies</li></ul>
  <h5 style="left:408px">SERVICES</h5>
  <ul style="left:408px"><li>Company Services</li><li>Personal Services</li><li>Advisory Services</li></ul>
  <h5 style="left:523px">WHO WE HELP</h5>
  <ul style="left:523px"><li>Property Investors and</li><li>Developers</li><li>Consultants</li><li>Medical Professionals</li><li>Buying or Selling a</li><li>Business</li></ul>
  <div class="contact">
    <div><svg width="9" height="11"><path d="M4.5 11C1 7 0 5 0 4a4.5 4.5 0 019 0c0 1-1 3-4.5 7z" fill="#14A79D"/></svg><span>12 Harbour Row, Market Street, England, AB1 2CD</span></div>
    <div><svg width="9" height="9"><path d="M1 1l2-1 2 3-1 1c.5 1.5 1.5 2.5 3 3l1-1 3 2-1 2C4 10-1 5 1 1z" fill="#14A79D"/></svg><span>+44 0100 555 210</span></div>
    <div><svg width="10" height="8"><rect x=".5" y=".5" width="9" height="7" fill="none" stroke="#14A79D"/><path d="M.5.5l4.5 4 4.5-4" fill="none" stroke="#14A79D"/></svg><span>hello@tolvard-mail.com</span></div>
    <div style="display:block">Company No.: 00000000<br>Registered office address:<br>8 Mill Lane, Ashford, AB2 3EF</div>
  </div>
  <h5 style="left:853px">SUBSCRIBE TO OUR NEWSLETTER</h5>
  <div class="input">Enter your email</div>
  <div class="btn" style="left:853px;top:128px;width:235px;height:32px;font-family:'Poppins',sans-serif;text-transform:none;font-size:10px;font-weight:600">Subscribe Newsletter</div>
  <div class="rule"></div>
  <div class="legal">PRIVACY POLICY &nbsp;|&nbsp; COOKIES POLICY &nbsp;|&nbsp; TERMS OF BUSINESS</div>
</footer>

</body>
</html>
```